Business cards for Wendcycle

We need a business card layout for our new bike and e-bike rental (we also sell used e-bikes and bike accessories). The logo already exists.

```html
<!DOCTYPE html>
<html lang="en">
<head>
<meta charset="utf-8">
<title>Wendcycle – Business Cards</title>
<link rel="stylesheet" href="https://fonts.googleapis.com/css2?family=Ubuntu:wght@400;500&family=Open+Sans:wght@400;600&display=swap">
<style>
  :root {
    --teal: #5ec5a6;
    --teal-deep: #4fb897;
    --ink: #2c3a45;
    --text: #5b6168;
    --paper: #fbfbfa;
    --backdrop: #e7e4df;
  }
  * { box-sizing: border-box; margin: 0; padding: 0; }
  html, body { width: 1200px; height: 886px; overflow: hidden; }
  body {
    background: var(--backdrop);
    display: flex;
    align-items: center;
    justify-content: center;
    gap: 90px;
    font-family: "Open Sans", Arial, sans-serif;
  }
  .card {
    position: relative;
    width: 380px;
    height: 620px;
    background: var(--paper);
    overflow: hidden;
    box-shadow: 0 10px 30px rgba(0,0,0,0.18);
  }
  .card__band {
    position: absolute;
    left: 0; top: 0;
    width: 100%;
    height: 232px;
    background: linear-gradient(135deg, var(--teal) 0%, var(--teal-deep) 100%);
  }

  /* front */
  .brand__dot {
    position: absolute;
    right: 96px; top: 44px;
    width: 32px; height: 32px;
    border-radius: 50%;
    background: var(--ink);
  }
  .brand__name {
    position: absolute;
    left: 0; right: 0; top: 96px;
    text-align: center;
    font-family: "Ubuntu", sans-serif;
    font-weight: 400;
    font-size: 54px;
    letter-spacing: 2px;
    color: #fff;
    line-height: 1;
  }
  .brand__tagline {
    position: absolute;
    left: 84px; top: 176px;
    font-family: "Ubuntu", sans-serif;
    font-weight: 500;
    font-size: 17px;
    color: var(--ink);
  }
  .person {
    position: absolute;
    left: 38px; bottom: 36px;
    writing-mode: vertical-rl;
    transform: rotate(180deg);
  }
  .person__name {
    font-size: 20px;
    font-weight: 400;
    color: var(--teal);
    letter-spacing: 0.5px;
    line-height: 1.15;
  }
  .person__role {
    font-size: 14px;
    font-weight: 600;
    color: var(--ink);
    line-height: 1.2;
  }
  .contact {
    position: absolute;
    left: 190px; bottom: 36px;
    writing-mode: vertical-rl;
    transform: rotate(180deg);
    list-style: none;
    font-size: 14px;
    color: var(--text);
    line-height: 1.35;
  }
  .contact li { display: flex; align-items: center; gap: 8px; }
  .contact__icon { width: 12px; height: 12px; transform: rotate(90deg); flex: none; }
  .contact__address { padding-bottom: 20px; }
  .accent-bar {
    position: absolute;
    left: 0; bottom: 0;
    width: 42px; height: 10px;
    background: var(--teal);
  }

  /* back */
  .emblem {
    position: absolute;
    left: 0; right: 0; top: 72px;
    display: flex;
    align-items: center;
    justify-content: center;
    gap: 14px;
  }
  .emblem__dot {
    width: 30px; height: 30px;
    border-radius: 50%;
    background: var(--ink);
  }
  .emblem__name {
    font-family: "Ubuntu", sans-serif;
    font-weight: 500;
    font-size: 46px;
    color: var(--ink);
    letter-spacing: 1px;
  }
  .services {
    position: absolute;
    right: 34px; top: 300px;
    writing-mode: vertical-rl;
    font-size: 15px;
    color: var(--text);
    line-height: 1.45;
  }
</style>
</head>
<body>
  <article class="card card--front">
    <div class="card__band"></div>
    <span class="brand__dot"></span>
    <div class="brand__name">WENDCYCLE</div>
    <div class="brand__tagline">gemütlich unterwegs</div>

    <div class="person">
      <div class="person__name">LENA HARTWIG</div>
      <div class="person__role">CEO/FOUNDER</div>
    </div>

    <ul class="contact">
      <li class="contact__address">2140 Alder Court</li>
      <li class="contact__address">Fairbanks, Alaska 99712</li>
      <li>
        <svg class="contact__icon" viewBox="0 0 12 12"><path d="M2 1l2 0 1 3-1.5 1a6 6 0 0 0 3 3L7.5 6.5l3 1 0 2-1 1A9 9 0 0 1 1 2z" fill="var(--teal)"/></svg>
        555 214 3087
      </li>
      <li>
        <svg class="contact__icon" viewBox="0 0 12 12"><rect x="1" y="2" width="10" height="8" fill="none" stroke="var(--teal)" stroke-width="1.3"/></svg>
        555 730 1642
      </li>
      <li>
        <svg class="contact__icon" viewBox="0 0 12 12"><rect x="3" y="0.5" width="6" height="11" rx="1" fill="var(--teal)"/></svg>
        555 918 4275
      </li>
      <li>
        <svg class="contact__icon" viewBox="0 0 12 12"><rect x="1" y="1" width="10" height="10" rx="1" fill="var(--teal)"/><path d="M2.5 3.5l3.5 3 3.5-3" stroke="#fff" stroke-width="1" fill="none"/></svg>
        lena@wendcycle.com
      </li>
      <li>
        <svg class="contact__icon" viewBox="0 0 12 12"><circle cx="6" cy="6" r="5" fill="var(--teal)"/><path d="M1 6h10M6 1c-2 3-2 7 0 10M6 1c2 3 2 7 0 10" stroke="#fff" stroke-width="0.8" fill="none"/></svg>
        www.wendcycle.com
      </li>
    </ul>
    <div class="accent-bar"></div>
  </article>

  <article class="card card--back">
    <div class="card__band"></div>
    <div class="emblem">
      <span class="emblem__dot"></span>
      <span class="emblem__name">WENDCYCLE</span>
    </div>
    <p class="services">New bike &amp; e-bike rental<br>used e-bikes &amp; bike accessories</p>
  </article>
</body>
</html>
```